Simple+Professional tech feel + warm and friendly box design for pet test kit

Project Name: 10-Minute Canine & Feline Rapid Test Kit Packaging Design
Target Brand Reference: VETRALUX (South Korea) styles
Design Style Direction: Professional tech feel + warm and friendly
Professionalism (Professional): Clear typography and distinct information hierarchy to reflect the product’s scientific rigor and accuracy.
Technological: Reflected through clean graphics and a minimalist layout.
Friendly: Utilise soft, warm colour combinations to convey care for pets and well-wishes for their health.
International: The design should align with mainstream aesthetics and avoid cultural ambiguities.

Target Market(s)
European Union and the United States
Industry/Entity Type
Veterinary Medical
Look and feel
Each slider illustrates characteristics of the customer's brand and the style your logo design should communicate.

```html
<!DOCTYPE html>
<html lang="en">
<head>
<meta charset="UTF-8">
<title>Petlucid 10-minute Canine &amp; Feline Rapid Test Kit</title>
<link rel="stylesheet" href="https://fonts.googleapis.com/css2?family=DM+Sans:wght@400;600;700&family=Cormorant+Garamond:wght@500&display=swap">
<style>
  :root {
    --backdrop: #dedede;
    --panel: #fafafa;
    --teal: #1fa99f;
    --orange: #f0962a;
    --ink-grey: #5a5a5a;
    --white: #ffffff;
  }
  * { margin: 0; padding: 0; box-sizing: border-box; }
  html, body {
    width: 1200px; height: 701px; overflow: hidden;
    background: var(--backdrop);
  }
  .front-panel {
    position: absolute; left: 180px; top: 70px;
    width: 840px; height: 561px;
    background: var(--panel);
    box-shadow: 0 6px 24px rgba(0,0,0,0.08);
    font-family: "DM Sans", Arial, sans-serif;
  }
  .brand-band {
    position: absolute; left: 0; top: 0;
    width: 156px; height: 100%;
    background: var(--teal);
  }
  .maker-name {
    position: absolute; top: 50px; left: 0; width: 156px;
    text-align: center;
    font-family: "Cormorant Garamond", Georgia, serif;
    font-weight: 500; font-size: 30px; color: var(--white);
    letter-spacing: 0.5px;
  }
  .product-title {
    position: absolute; left: 199px; top: 52px;
    font-weight: 600; font-size: 42px; line-height: 1.15;
    color: var(--teal); letter-spacing: -0.3px;
  }
  .product-subtitle {
    position: absolute; left: 199px; top: 190px;
    font-weight: 400; font-size: 28px; color: var(--ink-grey);
  }
  .test-count {
    position: absolute; left: 199px; top: 268px;
    width: 162px; height: 46px; border-radius: 12px;
    background: var(--orange); color: var(--white);
    font-size: 22px; font-weight: 400;
    display: flex; align-items: center; justify-content: center;
  }
  .pet-artwork {
    position: absolute; left: 571px; top: 273px;
    width: 232px; height: 224px; border-radius: 8px;
    background: linear-gradient(160deg, rgba(31,169,159,0.18), rgba(31,169,159,0.06));
  }
  .product-brand {
    position: absolute; left: 210px; top: 448px;
    font-weight: 700; font-size: 46px; color: var(--teal);
    letter-spacing: -0.5px;
  }
</style>
</head>
<body>
  <main class="front-panel">
    <div class="brand-band">
      <p class="maker-name">Orlinde</p>
    </div>
    <h1 class="product-title">10-minute Canine<br>&amp; Feline Rapid Test Kit</h1>
    <p class="product-subtitle">For Dogs and Cats</p>
    <div class="test-count">5 Tests/Kit</div>
    <div class="pet-artwork" role="img" aria-label="Teal line illustration of a seated dog and cat side by side"></div>
    <p class="product-brand">Petlucid</p>
  </main>
</body>
</html>
```